Building quality affordable homes in Brisbane, Australia for investors and families

We design, build and market our own homes from small single story to large 3 story luxury homes. Our main focus is "duel key" - that is two houses on one lot - a "gribby" (as in where The Gribbs lived) or attached granny flat.
We have a logo design and need a business card to suit. Something simple but eye catching. We want to communicate: "you are making a smart financial choice buying or building with us".
Unfortunately a lot of information has to be on the card including - Name, position, phone, mobile, fax, email, web address and of course the logo.
Logo in multiple formats and high res now available.

Target Market(s)

Families, contractors, real estate agents, other builders, developers, banks and home buyers.

Industry/Entity Type

Financial

Contact Information for Business Card

Name, position, phone, mobile, fax, email, web address

Font styles to use
Serif

Requirements
Must have
• The logo, and the details.
Nice to have
• Show or explain what we do - design, build and market affordable homes.
Should not have
• Nothing too fancy, outrageous - building companies are normally very straight.

```html
<!DOCTYPE html>
<html lang="en">
<head>
<meta charset="utf-8">
<title>Stonebridge Homes – Business Card</title>
<link rel="stylesheet" href="https://fonts.googleapis.com/css2?family=Open+Sans:wght@400;600;700&display=swap">
<style>
  :root {
    --page: #ecebe8;
    --card: #ffffff;
    --brand-blue: #1a7cc0;
    --brand-soft: #8fb4e0;
    --ink: #4a4a4a;
    --ink-soft: #5d5d5d;
  }
  * { box-sizing: border-box; margin: 0; padding: 0; }
  html, body { width: 1200px; height: 914px; overflow: hidden; }
  body {
    background: var(--page);
    font-family: "Open Sans", Arial, sans-serif;
    display: flex;
    flex-direction: column;
    align-items: center;
    justify-content: center;
    gap: 38px;
  }
  .card {
    width: 735px;
    height: 420px;
    background: var(--card);
    box-shadow: 0 2px 10px rgba(0,0,0,0.12);
    position: relative;
  }

  /* Brand lockup */
  .brand { display: flex; align-items: center; gap: 14px; }
  .brand-square { width: 58px; height: 58px; background: var(--brand-soft); flex: none; }
  .brand-name {
    color: var(--brand-blue);
    font-weight: 700;
    line-height: 1.05;
  }
  .brand-name .word { display: block; font-size: 40px; letter-spacing: -0.5px; }
  .brand-name .tag { display: block; font-size: 13px; letter-spacing: 1px; }

  /* Back */
  .card-back { display: flex; align-items: center; justify-content: center; }

  /* Front */
  .card-front { display: flex; }
  .front-brand {
    width: 50%;
    display: flex;
    align-items: center;
    justify-content: center;
  }
  .divider {
    position: absolute;
    left: 50%;
    top: 60px;
    bottom: 60px;
    width: 2px;
    background: var(--brand-blue);
  }
  .front-details {
    width: 50%;
    padding: 98px 0 0 52px;
  }
  .person-name { font-size: 28px; font-weight: 600; color: var(--ink); line-height: 1.1; }
  .person-role { font-size: 14px; color: var(--ink-soft); margin-top: 2px; }
  .contact-list { list-style: none; margin-top: 26px; }
  .contact-list li {
    display: flex; align-items: center; gap: 14px;
    font-size: 17px; color: var(--ink); height: 27px;
  }
  .contact-list svg { width: 17px; height: 17px; fill: var(--brand-blue); flex: none; }
</style>
</head>
<body>

<section class="card card-back">
  <div class="brand">
    <div class="brand-square"></div>
    <div class="brand-name"><span class="word">Stonebridge</span><span class="tag">HOMES PTY LTD</span></div>
  </div>
</section>

<section class="card card-front">
  <div class="front-brand">
    <div class="brand">
      <div class="brand-square"></div>
      <div class="brand-name"><span class="word">Stonebridge</span><span class="tag">HOMES PTY LTD</span></div>
    </div>
  </div>
  <div class="divider"></div>
  <div class="front-details">
    <h1 class="person-name">Marcus Kelby</h1>
    <p class="person-role">Managing Director</p>
    <ul class="contact-list">
      <li><svg viewBox="0 0 16 16"><circle cx="8" cy="4.5" r="3.5"/><path d="M1 16c0-4 3-6.5 7-6.5s7 2.5 7 6.5z"/></svg>07 3555 0142</li>
      <li><svg viewBox="0 0 16 16"><path d="M4 1l3 3-2 2c1 2 3 4 5 5l2-2 3 3-2 3C7 15 1 9 1 3z"/></svg>0412 555 876</li>
      <li><svg viewBox="0 0 16 16"><rect x="4" y="1" width="8" height="4"/><rect x="1" y="6" width="14" height="6" rx="1"/><rect x="4" y="10" width="8" height="5"/></svg>07 3555 0143</li>
      <li><svg viewBox="0 0 16 16"><path d="M1 3h14v10H1z M2 4l6 5 6-5" fill="none" stroke="#1a7cc0" stroke-width="1.6"/></svg>info@stonebridgehomes.com.au</li>
      <li><svg viewBox="0 0 16 16"><circle cx="8" cy="8" r="7"/><path d="M1 8h14M8 1c-3 4-3 10 0 14M8 1c3 4 3 10 0 14" fill="none" stroke="#fff" stroke-width="1"/></svg>www.stonebridgehomes.com.au</li>
    </ul>
  </div>
</section>

</body>
</html>
```